Tech Company Letterhead/Business Cards/Envelopes

We would like a new stationary design for a technology company that develops full turnkey solutions for governments related to Data, Identity Tracking, Fingerprinting, Passport Control, and Border Protection Systems.

We would like the stationary designs to include:

Letter Head
Business Cards
Envelopes

Target Market(s)

Corporate

Industry/Entity Type

Business

Contact Information for Business Card

Details to be shared with the winner.

Font styles to use
Serif
Sans Serif

Colors
e4daeb
85abd2
3176b5
0355a3
0692cd

```html
<!DOCTYPE html>
<html lang="en">
<head>
<meta charset="utf-8">
<title>Norvex Stationery</title>
<link href="https://fonts.googleapis.com/css2?family=PT+Sans:wght@400;700&display=swap" rel="stylesheet">
<style>
  :root {
    --backdrop: #ececec;
    --paper: #f8f8f8;
    --brand-blue: #2272b0;
    --accent-grey: #656565;
    --ink: #3a3a3a;
    --ink-soft: #555555;
    --white: #ffffff;
  }
  * { margin: 0; padding: 0; box-sizing: border-box; }
  html, body { width: 1200px; height: 1005px; overflow: hidden; }
  body {
    background: var(--backdrop);
    font-family: "PT Sans", sans-serif;
    color: var(--ink);
    position: relative;
  }
  .sheet { position: absolute; background: var(--paper); }
  .brand-name {
    font-family: "PT Sans", sans-serif;
    font-weight: 700;
    letter-spacing: 2px;
    line-height: 1;
    color: var(--brand-blue);
  }
  .brand-bar { position: absolute; left: 0; right: 0; bottom: 0; height: 6px; display: flex; }
  .brand-bar span { height: 100%; }
  .bar-blue { background: var(--brand-blue); }
  .bar-grey { background: var(--accent-grey); }
  .bar-white { background: var(--white); }

  /* Letterhead */
  .letterhead { left: 167px; top: 85px; width: 400px; height: 567px; }
  .letterhead .brand-name { position: absolute; left: 38px; top: 43px; font-size: 23px; }
  .letterhead-contact {
    position: absolute; right: 26px; top: 40px;
    display: flex; gap: 6px; font-size: 7.5px; line-height: 10.5px; color: var(--ink-soft);
  }
  .contact-address { text-align: right; }
  .contact-lines div { display: flex; align-items: center; gap: 4px; }
  .contact-lines svg { width: 6px; height: 6px; fill: var(--brand-blue); }
  .letter-body { position: absolute; left: 36px; top: 153px; width: 331px; }
  .salutation { font-size: 13px; margin-bottom: 22px; color: var(--ink); }
  .letter-body p {
    font-size: 6.3px; line-height: 8.6px; text-align: justify;
    color: var(--ink-soft); margin-bottom: 8px;
  }
  .closing { font-size: 6.5px; margin-top: 16px; color: var(--ink-soft); }
  .signature-area {
    width: 56px; height: 20px; margin-top: 4px;
    background: linear-gradient(90deg, #e8e8e8, #f2f2f2);
  }
  .letterhead-web {
    position: absolute; left: 0; right: 0; top: 538px; text-align: center;
    font-size: 7px; letter-spacing: 3px; color: var(--ink-soft);
  }

  /* Folder */
  .folder { left: 636px; top: 58px; width: 472px; height: 597px; background: var(--brand-blue); }
  .folder-spine {
    position: absolute; left: 4px; top: 0; bottom: 9px; width: 24px;
    border-left: 1px solid rgba(0,0,0,0.18); border-right: 1px solid rgba(0,0,0,0.12);
  }
  .folder .brand-name {
    position: absolute; left: 0; right: 0; top: 274px; text-align: center;
    font-size: 60px; letter-spacing: 8px; color: var(--white);
  }
  .folder-web {
    position: absolute; left: 0; right: 0; top: 561px; text-align: center;
    font-size: 7px; letter-spacing: 3px; color: var(--white);
  }
  .folder .brand-bar { height: 9px; }

  /* Compliment slip */
  .slip { left: 167px; top: 715px; width: 448px; height: 215px; }
  .slip .brand-name { position: absolute; left: 23px; top: 22px; font-size: 23px; }
  .slip-address {
    position: absolute; left: 23px; top: 55px;
    font-size: 7px; line-height: 9px; color: var(--ink-soft);
  }

  /* Envelope */
  .envelope { left: 658px; top: 717px; width: 448px; height: 218px; }
  .envelope-flap { position: absolute; left: 0; top: 0; width: 448px; height: 80px; }
  .envelope .brand-name {
    position: absolute; left: 0; right: 0; top: 26px; text-align: center;
    font-size: 18px; letter-spacing: 2px; color: var(--white);
  }
  .envelope-web {
    position: absolute; left: 0; right: 0; top: 46px; text-align: center;
    font-size: 6.5px; letter-spacing: 2.5px; color: var(--white);
  }
</style>
</head>
<body>

<section class="sheet letterhead">
  <div class="brand-name">NORVEX</div>
  <div class="letterhead-contact">
    <div class="contact-address">
      <div>4120 Larkspur Road</div>
      <div>Juneau</div>
      <div>Alaska 99801</div>
    </div>
    <div class="contact-lines">
      <div><svg viewBox="0 0 10 10"><path d="M2 0h2l1 3-1.5 1a6 6 0 0 0 2.5 2.5L7 5l3 1v2c0 1-1 2-2 2A8 8 0 0 1 0 2c0-1 1-2 2-2z"/></svg>555 204 7731</div>
      <div><svg viewBox="0 0 10 10"><path d="M2 0h6v3H2zM0 4h10v4H8v2H2V8H0z"/></svg>555 318 6642</div>
      <div><svg viewBox="0 0 10 10"><path d="M0 2h10v6H0zM0 2l5 3.5L10 2" /></svg>hello@norvex.com</div>
    </div>
  </div>

  <div class="letter-body">
    <div class="salutation">Dear Mr. Hale,</div>
    <p>Thank you for meeting with our team last week to review the plans for the new border control program. We were glad to hear your views on data security, identity checks and the timeline for the first stage. This letter sets out the next steps we agreed on and the people who will lead each part of the work on our side.</p>
    <p>Our engineers will visit your offices in early spring to survey the current passport desks and network rooms. After the visit we will share a short report with a plan for hardware, software and staff training, along with a clear budget for each phase of the rollout.</p>
    <p>We will also set up a test site where your officers can try the new fingerprint readers and give us feedback before full launch. Any changes you ask for at this stage will be built into the final system at no extra cost, so that the tools fit the way your teams already work each day.</p>
    <p>Please let us know if the dates above suit your schedule. We look forward to working with you and your team on this project and to a long and useful partnership in the years ahead.</p>
    <div class="closing">Sincerely,</div>
    <div class="signature-area" role="img" aria-label="Handwritten signature"></div>
  </div>

  <div class="letterhead-web">www.norvex.com</div>
  <div class="brand-bar">
    <span class="bar-blue" style="width:64px"></span>
    <span class="bar-grey" style="width:152px"></span>
    <span class="bar-blue" style="width:33px"></span>
    <span class="bar-grey" style="flex:1"></span>
  </div>
</section>

<section class="sheet folder">
  <div class="folder-spine"></div>
  <div class="brand-name">NORVEX</div>
  <div class="folder-web">www.norvex.com</div>
  <div class="brand-bar">
    <span class="bar-white" style="width:61px"></span>
    <span class="bar-grey" style="width:187px"></span>
    <span class="bar-white" style="width:42px"></span>
    <span class="bar-grey" style="flex:1"></span>
  </div>
</section>

<section class="sheet slip">
  <div class="brand-name">NORVEX</div>
  <div class="slip-address">
    <div>4120 Larkspur Road</div>
    <div>Juneau, Alaska 99801</div>
  </div>
  <div class="brand-bar">
    <span class="bar-blue" style="width:74px"></span>
    <span class="bar-grey" style="width:170px"></span>
    <span class="bar-blue" style="width:38px"></span>
    <span class="bar-grey" style="flex:1"></span>
  </div>
</section>

<section class="sheet envelope">
  <svg class="envelope-flap" viewBox="0 0 448 80" aria-hidden="true">
    <path d="M0 0H448V70Q448 78 440 79H8Q0 78 0 70Z" fill="var(--brand-blue)"/>
  </svg>
  <div class="brand-name">NORVEX</div>
  <div class="envelope-web">www.norvex.com</div>
</section>

</body>
</html>
```